Creative, fresh business card design for Orrin Linings

We need a fresh, creative business card design for Orrin Linings. We are the manufacturer of Orrin Linings in Australia. Wall panels are 2400 x 1200mm panels made from MDF and feature 3D patterns on the face of the panel. The colours to be used are green, silver/grey and white RGB
Red 187
Green 207
Blue 65.

An idea is to possibly use a watermark of one of our designs as a background (like on the "Ferns" design on the left hand side of page 2 of our brochure).

Target Market(s)

Interior designers, architects, builders and home renovators

Industry/Entity Type

Business

Contact Information for Business Card

Details to go on the card are:
Our logo (attached),
Slogan: "Decorative panels for interiors and exteriors",
Contact name,
Position,
Mobile phone number,
Business address,
Business phone,
Business fax,
Website and
Email address.

I have attached a few images of our panels and our brochure for reference.

The colours of the business card should feature our logo colours which are: RGB
Red 187
Green 207
Blue 65

Requirements
Must have
• Very modern fonts and design. Some of the designs shown especially the "Weave" design which is a popular design.
Nice to have
• Creative but simple design. Very contemporary.
Should not have
• Anything ornate or old fashioned.

```html
<!DOCTYPE html>
<html lang="en">
<head>
<meta charset="utf-8">
<title>Orrin Linings — Business Card</title>
<link href="https://fonts.googleapis.com/css2?family=Open+Sans:wght@300;400;600;700&display=swap" rel="stylesheet">
<style>
  :root {
    --brand-green: rgb(187, 207, 65);
    --ink-black: #0d0d0d;
    --card-black: #151515;
    --silver: #a9a9ab;
    --silver-dark: #8c8c8e;
    --card-white: #e9e9ea;
    --text-grey: #6a6a6c;
    --page-bg: #f2f2f2;
  }
  * { box-sizing: border-box; margin: 0; padding: 0; }
  html, body {
    width: 1200px; height: 900px; overflow: hidden;
    background: var(--page-bg);
    font-family: "Open Sans", Arial, sans-serif;
  }
  .stage { position: relative; width: 1200px; height: 900px; }

  .card {
    position: absolute; left: 260px; width: 680px; height: 389px;
    border-radius: 22px; overflow: hidden;
    box-shadow: 0 6px 18px rgba(0,0,0,0.18);
  }
  .card-front { top: 40px; background: var(--card-black); }
  .card-back { top: 471px; background: var(--card-white); }

  .panel-texture { position: absolute; inset: 0; }
  .card-front .panel-texture {
    background: radial-gradient(ellipse at 55% 45%, #262626 0%, #141414 55%, #050505 100%);
  }
  .card-back .panel-texture {
    background: linear-gradient(135deg, #eeeeef 0%, #e3e3e4 60%, #dcdcdd 100%);
  }

  /* front */
  .front-brand {
    position: absolute; left: 0; right: 0; top: 120px;
    display: flex; flex-direction: column; align-items: center;
  }
  .brand-mark { display: flex; align-items: center; gap: 14px; }
  .brand-square { width: 44px; height: 44px; background: var(--brand-green); }
  .brand-name {
    font-weight: 600; font-size: 40px; color: var(--brand-green); letter-spacing: 0.5px;
  }
  .front-slogan {
    margin-top: 22px; color: var(--silver);
    font-weight: 400; font-size: 17px; letter-spacing: 2.5px; line-height: 1.35; text-align: left;
  }

  /* back */
  .back-brand { position: absolute; left: 40px; top: 90px; }
  .back-brand .brand-square { width: 34px; height: 34px; }
  .back-brand .brand-name { font-size: 30px; }

  .contact-block { position: absolute; left: 360px; top: 120px; width: 290px; }
  .contact-name { font-size: 24px; font-weight: 300; color: var(--text-grey); line-height: 1; }
  .contact-name strong { font-weight: 700; }
  .contact-title { font-size: 14px; color: var(--brand-green); margin-top: 4px; }
  .divider { height: 2px; background: var(--brand-green); margin: 10px 0 14px; }
  .contact-columns { display: flex; gap: 22px; }
  .contact-list { list-style: none; }
  .contact-list li {
    display: flex; align-items: center; gap: 8px;
    font-size: 13px; color: var(--text-grey); margin-bottom: 9px; white-space: nowrap;
  }
  .contact-list svg { width: 13px; height: 13px; flex: none; fill: var(--brand-green); }
</style>
</head>
<body>
<main class="stage">

  <section class="card card-front">
    <div class="panel-texture" role="img" aria-label="Dark faceted 3D star wall panel pattern"></div>
    <div class="front-brand">
      <div class="brand-mark">
        <span class="brand-square"></span>
        <span class="brand-name">Orrin Linings</span>
      </div>
      <p class="front-slogan">decorative panels for<br>interiors &amp; landscapes</p>
    </div>
  </section>

  <section class="card card-back">
    <div class="panel-texture" role="img" aria-label="Faint light grey triangular wall panel pattern"></div>
    <div class="back-brand">
      <div class="brand-mark">
        <span class="brand-square"></span>
        <span class="brand-name">Orrin Linings</span>
      </div>
    </div>

    <div class="contact-block">
      <p class="contact-name">Your <strong>Name</strong></p>
      <p class="contact-title">JobTitle</p>
      <div class="divider"></div>
      <div class="contact-columns">
        <ul class="contact-list">
          <li><svg viewBox="0 0 16 16"><rect x="4" y="1" width="8" height="14" rx="1.5"/></svg>0000 0000 00</li>
          <li><svg viewBox="0 0 16 16"><path d="M2 5c0-2 2-3 6-3s6 1 6 3v1h-3V5H5v1H2zM3 8h10v6H3z"/></svg>0000 0000 00</li>
          <li><svg viewBox="0 0 16 16"><rect x="4" y="2" width="8" height="4"/><rect x="2" y="6" width="12" height="8" rx="1"/></svg>0000 0000 00</li>
        </ul>
        <ul class="contact-list">
          <li><svg viewBox="0 0 16 16"><rect x="1" y="3" width="14" height="10" rx="1"/></svg>youremail@xyz.com</li>
          <li><svg viewBox="0 0 16 16"><circle cx="8" cy="8" r="7"/></svg>yourwebsite.com</li>
          <li><svg viewBox="0 0 16 16"><path d="M8 1a5 5 0 0 1 5 5c0 4-5 9-5 9S3 10 3 6a5 5 0 0 1 5-5z"/></svg>youraddress</li>
        </ul>
      </div>
    </div>
  </section>

</main>
</body>
</html>
```